InfoGraphic for Security Pyramid

I've created an infographic that I would like to be redone more professionally. you can see the page in this powerpoint called the pyramid of security. What I'd like done is to replace the background graphic with a new icon in a cartoony format like the one behind end point protection as an example (thats a stock photo).

Target Market(s)

Business Owners

Font styles to use
Sans Serif

Colors
ec1f27
0355a3
f37122

Requirements
Must have
• Consistent images, text must be editable.

```html
<!DOCTYPE html>
<html lang="en">
<head>
<meta charset="utf-8">
<title>Pyramid of Security</title>
<link rel="stylesheet" href="https://fonts.googleapis.com/css2?family=Open+Sans:wght@400;600;700;800&display=swap">
<style>
  :root {
    --red: #ec1f27;
    --blue: #0355a3;
    --orange: #f37122;
    --ink-red: #7d1116;
    --ink-blue: #0f2b4c;
    --ink-orange: #7e2a0c;
    --white: #ffffff;
  }
  html, body {
    margin: 0;
    padding: 0;
    width: 1200px;
    height: 1200px;
    overflow: hidden;
    background: var(--white);
  }
  .canvas { display: block; width: 1200px; height: 1200px; }
  .brand-name { font-family: "Open Sans", sans-serif; font-weight: 800; font-size: 64px; fill: var(--red); }
  .brand-tagline { font-family: "Open Sans", sans-serif; font-weight: 700; font-size: 24px; fill: var(--orange); }
  .title { font-family: "Open Sans", sans-serif; font-weight: 700; font-size: 64px; fill: var(--red); }
  .tier-red { fill: var(--red); }
  .tier-blue { fill: var(--blue); }
  .tier-orange { fill: var(--orange); }
  .label { font-family: "Open Sans", sans-serif; font-weight: 400; font-size: 20px; fill: var(--white); text-anchor: middle; }
  .pin-text { font-family: "Open Sans", sans-serif; font-weight: 700; font-size: 22px; fill: var(--red); text-anchor: middle; }
  .icon-red { fill: none; stroke: var(--ink-red); stroke-width: 5; stroke-linecap: round; stroke-linejoin: round; }
  .icon-blue { fill: none; stroke: var(--ink-blue); stroke-width: 5; stroke-linecap: round; stroke-linejoin: round; }
  .icon-orange { fill: none; stroke: var(--ink-orange); stroke-width: 4; stroke-linecap: round; stroke-linejoin: round; }
  .solid-red { fill: var(--ink-red); }
  .solid-blue { fill: var(--ink-blue); }
  .solid-orange { fill: var(--ink-orange); }
</style>
</head>
<body>
<svg class="canvas" viewBox="0 0 1500 1500" xmlns="http://www.w3.org/2000/svg">

  <!-- Brand -->
  <g class="brand">
    <text class="brand-name" x="48" y="178">Corvane Networks</text>
    <text class="brand-tagline" x="48" y="240">Planning Protection Peace of Mind</text>
  </g>

  <text class="title" x="742" y="190" textLength="712" lengthAdjust="spacingAndGlyphs">PYRAMID OF SECURITY</text>

  <!-- Tier 1 -->
  <g class="tier">
    <polygon class="tier-orange" points="752,348 889,548 615,548"/>
    <g class="icon-orange">
      <polyline points="713,465 713,428 790,428 790,448"/>
    </g>
    <g class="solid-orange">
      <circle cx="726" cy="480" r="7"/><circle cx="751" cy="480" r="7"/><circle cx="775" cy="480" r="7"/>
      <path d="M714 497 a12 9 0 0 1 24 0z M739 497 a12 9 0 0 1 24 0z M763 497 a12 9 0 0 1 24 0z"/>
      <circle cx="788" cy="455" r="8"/><path d="M776 478 a12 12 0 0 1 24 0z"/>
      <rect x="733" y="478" width="10" height="3"/><rect x="758" y="478" width="10" height="3"/>
    </g>
    <text class="label" x="752" y="525">User Training</text>
  </g>

  <!-- Tier 2 -->
  <g class="tier">
    <polygon class="tier-blue" points="611,563 747,563 747,763 480,763"/>
    <polygon class="tier-blue" points="758,563 893,563 1024,763 758,763"/>
    <g class="icon-blue">
      <rect x="603" y="623" width="92" height="73" rx="4"/>
      <line x1="603" y1="638" x2="695" y2="638"/>
      <line x1="628" y1="650" x2="670" y2="650"/><line x1="628" y1="662" x2="670" y2="662"/><line x1="628" y1="675" x2="670" y2="675"/>
      <path d="M828 620 A45 45 0 0 1 900 640"/><path d="M890 690 A45 45 0 0 1 820 690"/>
      <path d="M814 672 A45 45 0 0 1 816 630"/><path d="M903 660 A45 45 0 0 1 898 680"/>
      <circle cx="858" cy="657" r="22"/>
    </g>
    <g class="solid-blue">
      <circle cx="654" cy="629" r="3"/><circle cx="668" cy="629" r="3"/><circle cx="682" cy="629" r="3"/>
      <circle cx="858" cy="657" r="9"/>
    </g>
    <text class="label" x="643" y="740">Web Filtering</text>
    <text class="label" x="880" y="740">Continuous Scanning</text>
  </g>

  <!-- Tier 3 -->
  <g class="tier">
    <polygon class="tier-orange" points="470,778 609,778 609,978 339,978"/>
    <polygon class="tier-orange" points="619,778 886,778 886,978 619,978"/>
    <polygon class="tier-orange" points="896,778 1034,778 1165,978 896,978"/>
    <g class="icon-orange">
      <rect x="486" y="840" width="54" height="54"/>
      <path d="M490 826v8 M502 822v12 M514 826v8 M526 822v12 M538 826v8 M490 900v8 M502 900v12 M514 900v8 M526 900v12 M538 900v8 M468 845h12 M472 857h8 M468 869h12 M472 881h8 M546 845h12 M546 857h8 M546 869h12 M546 881h8"/>
      <path d="M720 828h55l20 20v70h-76z"/>
      <circle cx="742" cy="851" r="17"/><line x1="730" y1="864" x2="708" y2="882"/>
      <line x1="740" y1="884" x2="760" y2="884"/><line x1="740" y1="892" x2="760" y2="892"/>
      <circle cx="778" cy="888" r="8"/>
      <rect x="958" y="835" width="80" height="80"/>
      <line x1="958" y1="850" x2="1038" y2="850"/>
      <path d="M1021 880l17 7v12c0 10-8 16-17 20-9-4-17-10-17-20v-12z"/>
    </g>
    <g class="solid-orange">
      <circle cx="513" cy="867" r="15"/>
      <rect x="720" y="905" width="76" height="13"/>
      <circle cx="1021" cy="896" r="6"/><path d="M1011 912a10 8 0 0 1 20 0z"/>
    </g>
    <text class="label" x="506" y="955">Threat Intel</text>
    <text class="label" x="753" y="955">Asset Management</text>
    <text class="label" x="1010" y="955">Minimize Admin</text>
  </g>

  <!-- Tier 4 -->
  <g class="tier">
    <polygon class="tier-blue" points="329,993 463,993 463,1193 198,1193"/>
    <polygon class="tier-blue" points="478,993 744,993 744,1193 478,1193"/>
    <polygon class="tier-blue" points="759,993 1025,993 1025,1193 759,1193"/>
    <polygon class="tier-blue" points="1040,993 1175,993 1306,1193 1040,1193"/>
    <g class="icon-blue">
      <rect x="330" y="1048" width="90" height="76" rx="6"/>
      <line x1="330" y1="1064" x2="420" y2="1064"/>
      <path d="M375 1075l17 7v12c0 10-8 16-17 20-9-4-17-10-17-20v-12z"/>
      <rect x="582" y="1040" width="50" height="86" rx="6"/>
      <line x1="582" y1="1115" x2="632" y2="1115"/>
      <path d="M860 1052h18v54h-18 M860 1080h18 M878 1062h10v40h-10 M888 1086h34"/>
      <path d="M1083 1052h72l-26 34v30l-20 8v-38z"/>
      <path d="M1140 1100h38 M1166 1088l12 12-12 12 M1170 1080h16v42h-16"/>
    </g>
    <g class="solid-blue">
      <circle cx="388" cy="1056" r="3"/><circle cx="398" cy="1056" r="3"/><circle cx="408" cy="1056" r="3"/>
      <rect x="622" y="1075" width="20" height="18" rx="2"/>
      <rect x="831" y="1042" width="28" height="14"/><rect x="831" y="1065" width="28" height="14"/>
      <rect x="831" y="1089" width="28" height="14"/><rect x="831" y="1113" width="28" height="14"/>
      <rect x="878" y="1054" width="28" height="14"/><rect x="878" y="1102" width="28" height="14"/>
      <rect x="924" y="1078" width="30" height="16"/>
    </g>
    <text class="label" x="349" y="1170">Next Gen Firewall</text>
    <text class="label" x="611" y="1170">Mobile Security</text>
    <text class="label" x="897" y="1170">SOPs</text>
    <text class="label" x="1141" y="1170">Logging</text>
  </g>

  <!-- Tier 5 -->
  <g class="tier">
    <polygon class="tier-red" points="188,1208 326,1208 326,1408 57,1408"/>
    <polygon class="tier-red" points="338,1208 605,1208 605,1408 338,1408"/>
    <polygon class="tier-red" points="617,1208 884,1208 884,1408 617,1408"/>
    <polygon class="tier-red" points="896,1208 1163,1208 1163,1408 896,1408"/>
    <polygon class="tier-red" points="1175,1208 1316,1208 1443,1408 1175,1408"/>
    <g class="icon-red">
      <path d="M247 1343h-58v-75h82v50"/>
      <line x1="189" y1="1284" x2="271" y2="1284"/>
      <line x1="197" y1="1302" x2="236" y2="1302"/><line x1="197" y1="1314" x2="230" y2="1314"/><line x1="197" y1="1326" x2="220" y2="1326"/>
      <path d="M253 1334a13 13 0 0 1 24-4 M279 1343a13 13 0 0 1-24 4"/>
      <path d="M506 1275a22 22 0 0 1 22 22 M506 1263a34 34 0 0 1 34 34"/>
      <path d="M704 1303v-30h100v10 M748 1273v-12"/>
      <path d="M718 1322a16 16 0 1 1-16-3"/>
      <path d="M993 1305v-40h14 M1052 1265h14v40 M1030 1310v8c0 6-8 6-8 12v6"/>
      <rect x="992" y="1322" width="74" height="28" rx="3"/>
      <rect x="1225" y="1268" width="86" height="66"/>
      <path d="M1225 1268l43 38 43-38 M1225 1334l30-30 M1311 1334l-30-30"/>
    </g>
    <g class="solid-red">
      <rect x="417" y="1292" width="90" height="54" rx="3"/>
      <circle cx="506" cy="1297" r="6"/>
      <rect x="752" y="1286" width="60" height="15" rx="3"/><rect x="752" y="1306" width="60" height="15" rx="3"/><rect x="752" y="1326" width="60" height="15" rx="3"/>
      <path d="M1030 1248l24 10v18c0 15-12 24-24 30-12-6-24-15-24-30v-18z"/>
      <rect x="1254" y="1320" width="28" height="26" rx="3"/>
      <path d="M1259 1320v-8a9 9 0 0 1 18 0v8" fill="none" stroke="var(--ink-red)" stroke-width="5"/>
    </g>
    <text class="pin-text" x="459" y="1330">***_</text>
    <text class="label" x="224" y="1386">Updating</text>
    <text class="label" x="471" y="1386">Passwords</text>
    <text class="label" x="750" y="1386">Backups</text>
    <text class="label" x="1029" y="1386">Endpoint Protection</text>
    <text class="label" x="1281" y="1386">Email Security</text>
  </g>
</svg>
</body>
</html>
```